TallyForge needs a new rocket based website

We need a new website that will be based on our rocket ship logo. We develop innovative solutions for enterprises. We would like to see a design that when the pages scroll, the rocket launches and goes from launch through a journey, similar to how we approach our customer. We would like areas for "Who are we", "What can we do", "What have we done", "How can we help". http://www.tallyforge.com.au is our current website

Target Market(s)

Government, Enterprise, Cloud

Industry/Entity Type

Software Service

Coding

Coded - Design and coding required

Number of Pages Required

2 page

Requirements
Must have
• We would like to see a design that when the pages scroll, the rocket launches and goes from launch through a journey, similar to how we approach our customer.
• Must have a home page and a detail page.
• Would like to see the logo/rocket animate in some way when you scroll through he page.

```html
<!DOCTYPE html>
<html lang="en">
<head>
<meta charset="utf-8">
<title>TallyForge – Innovative Software Solutions</title>
<link rel="stylesheet" href="https://fonts.googleapis.com/css2?family=Poppins:wght@400;500;600;700&display=swap">
<style>
:root{
  --orange:#f07a1a;
  --orange-deep:#e56a0c;
  --orange-soft:#fbd3a6;
  --ink:#1e1e1e;
  --body:#3b3b3b;
  --grey-bg:#f3f3f3;
  --dark:#1c1f24;
  --white:#ffffff;
}
*{box-sizing:border-box;margin:0;padding:0}
html,body{width:1200px;height:3689px;overflow:hidden;background:var(--white);font-family:'Poppins',sans-serif;color:var(--body)}
.page{position:relative;width:1200px;height:3689px;overflow:hidden}
.abs{position:absolute}

/* hero */
.hero-photo{left:0;top:0;width:1200px;height:680px;background:radial-gradient(ellipse at 60% 30%,#5a5450 0%,#2e2c2c 45%,#141516 100%)}
.hero-wave{left:0;top:630px;width:1200px;height:60px}
.brand{left:148px;top:58px;display:flex;align-items:center;gap:10px;font-weight:700;font-size:34px;color:var(--orange)}
.brand-dot{width:16px;height:16px;border-radius:50%;background:var(--orange)}
.nav{left:510px;top:66px;display:flex;gap:33px;font-weight:500;font-size:17px;color:var(--white);letter-spacing:.3px}
.nav .active{color:var(--orange)}
.hero-title{left:0;top:278px;width:1200px;text-align:center;font-weight:700;font-size:47px;line-height:58px;color:var(--white)}
.hero-title span{color:var(--orange)}
.btn-outline{display:inline-block;border:2px solid currentColor;border-radius:22px;font-weight:600;font-size:15px;padding:8px 22px}
.hero-btn{left:517px;top:420px;color:var(--white)}
.dots{left:567px;top:500px;display:flex;gap:8px}
.dots i{width:11px;height:11px;border-radius:50%;background:var(--white);opacity:.9}
.dots i:first-child{outline:2px solid var(--white);outline-offset:2px;background:transparent;border:3px solid var(--white)}

/* rockets */
.rocket{width:52px;height:150px;border-radius:26px 26px 12px 12px;background:linear-gradient(180deg,#f5a04a 0%,var(--orange) 55%,#ffcc66 100%)}

/* who */
.section-title{font-weight:700;font-size:36px;color:var(--ink);letter-spacing:.5px}
.who-title{left:143px;top:800px}
.text{font-size:14px;line-height:31px;color:var(--body)}
.who-text{left:143px;top:862px;width:460px}
.who-btn{left:143px;top:1068px;color:var(--ink);padding:6px 22px}
.laptop{left:648px;top:780px;width:448px;height:320px;border-radius:10px;background:linear-gradient(180deg,#2a3a6a 0%,#4a5a8c 55%,#d7dbe6 100%)}

/* what can we do */
.grey{left:0;top:1218px;width:1200px;height:792px;background:var(--grey-bg)}
.grey-curves{left:0;top:1200px;width:1200px;height:300px}
.wcwd{left:0;top:1368px;width:1200px;text-align:center;font-weight:400;font-size:37px;color:var(--ink)}
.wcwd b{font-weight:700}
.card{width:442px;height:196px;background:var(--white);box-shadow:0 2px 8px rgba(0,0,0,.18)}
.card .icon{position:absolute;left:20px;top:38px;width:96px;height:96px;border-radius:50%;background:var(--orange);display:flex;align-items:center;justify-content:center;box-shadow:0 0 0 4px var(--white),0 0 0 6px var(--orange)}
.card h3{position:absolute;left:136px;top:32px;font-weight:500;font-size:19px;color:var(--ink)}
.card p{position:absolute;left:136px;top:70px;width:280px;font-size:12px;line-height:25px}

/* done */
.done-photo{left:143px;top:2153px;width:424px;height:370px;background:linear-gradient(135deg,#c9ccd2 0%,#6a7180 50%,#2c3138 100%);border:6px solid var(--white);box-shadow:0 4px 14px rgba(0,0,0,.35)}
.done-title{left:624px;top:2182px}
.done-text{left:625px;top:2246px;width:450px;line-height:29px}
.done-btn{left:627px;top:2447px;color:var(--ink);padding:7px 22px}

/* help */
.help-bg{left:0;top:2660px;width:1200px;height:600px}
.help-title{left:0;top:2775px;width:1200px;text-align:center;font-weight:700;font-size:37px;color:var(--white);letter-spacing:.5px}
.field{background:var(--white);height:37px;font-size:11px;color:#555;padding:10px 16px}
.field.msg{height:142px}
.submit{left:480px;top:3104px;width:240px;height:44px;background:#222;color:var(--white);font-weight:600;font-size:15px;text-align:center;line-height:44px;border-radius:2px;letter-spacing:.5px}

/* footer */
.footer{left:0;top:3240px;width:1200px;height:352px;background:var(--grey-bg)}
.f-title{font-weight:600;font-size:17px;color:var(--ink)}
.f-title span{color:var(--orange)}
.f-text{font-size:12px;line-height:23px;color:var(--body)}
.f-input{left:143px;top:3428px;width:278px;height:38px;background:var(--white);border:1px solid #ccc;font-size:11px;padding:11px 12px;color:#666}
.f-btn{left:143px;top:3484px;width:116px;height:34px;background:#6e6e6e;color:var(--white);font-weight:600;font-size:13px;text-align:center;line-height:34px}
.contact-row{display:flex;gap:14px;align-items:flex-start}
.social{display:flex;gap:6px}
.social i{width:22px;height:22px;border-radius:50%;border:1.5px solid #555}
.links{list-style:none}
.links li{font-size:12px;line-height:26px}
.links li::before{content:"";display:inline-block;width:4px;height:4px;border-radius:50%;background:var(--ink);margin:0 10px 2px 0}
.copy{left:0;top:3622px;width:1200px;text-align:center;font-size:12px;color:var(--ink)}
</style>
</head>
<body>
<div class="page">

  <!-- hero -->
  <div class="abs hero-photo" role="img" aria-label="Team of developers gathered around a laptop"></div>
  <svg class="abs hero-wave" viewBox="0 0 1200 60" preserveAspectRatio="none" aria-hidden="true">
    <path d="M0 30 C40 10 70 45 110 28 S190 8 230 30 S310 50 350 26 S430 6 470 30 S550 48 590 24 S670 8 710 30 S790 50 830 26 S910 8 950 30 S1030 48 1070 26 S1150 10 1200 30 V60 H0Z" fill="#fff"/>
  </svg>
  <div class="abs brand"><span class="brand-dot"></span>TallyForge</div>
  <nav class="abs nav"><span class="active">HOME</span><span>ABOUT US</span><span>SERVICES</span><span>PRICING</span><span>CONTACT US</span></nav>
  <h1 class="abs hero-title"><span>INNOVATIVE</span> SOFTWARE<br>SOLUTIONS</h1>
  <span class="abs btn-outline hero-btn">GET MORE INFO</span>
  <div class="abs dots"><i></i><i></i><i></i><i></i></div>

  <!-- journey path -->
  <svg class="abs" style="left:0;top:0" width="1200" height="3689" aria-hidden="true">
    <g fill="none" stroke="#333" stroke-width="2" stroke-dasharray="2 5">
      <polyline points="592,740 592,746 868,746 868,790"/>
      <polyline points="868,1100 868,1173 600,1173 600,1185"/>
      <polyline points="600,1340 600,1975"/>
      <polyline points="600,2116 600,2600"/>
      <polyline points="620,2765 1073,2765 1073,3285 1010,3285 1010,3320"/>
    </g>
  </svg>

  <div class="abs rocket" style="left:566px;top:578px" role="img" aria-label="Rocket launching"></div>

  <!-- who are we -->
  <h2 class="abs section-title who-title">WHO ARE WE</h2>
  <p class="abs text who-text">Sed ut perspiciatis unde omnis iste natus error sit voluptatem alium doloremque laudantium, totam rem aperiam, eaque ipsa quae ab illo inventore veritatis et quasi architecto beatae vitae dicta sunt explicabo. Nemo enim ipsam voluptatem quia voluptas sit aspatur aut odit aut fugit, sed quia consequuntur magni dolores eos qui ratione voluptatem sequi nesciunt.</p>
  <span class="abs btn-outline who-btn">Read More</span>
  <div class="abs laptop" role="img" aria-label="Laptop with a rocket launching from its screen"></div>

  <!-- what can we do -->
  <div class="abs grey"></div>
  <svg class="abs grey-curves" viewBox="0 0 1200 300" preserveAspectRatio="none" aria-hidden="true">
    <path d="M0 18 C300 -10 520 0 620 30 C420 40 180 120 0 260Z" fill="var(--orange-soft)"/>
    <path d="M0 0 H1200 V60 C1000 -5 760 -10 600 38 C420 40 190 60 0 60Z" fill="#fff"/>
  </svg>
  <div class="abs rocket" style="left:574px;top:1180px" role="img" aria-label="Rocket in flight"></div>
  <h2 class="abs wcwd">WHAT <b>CAN WE DO</b></h2>

  <div class="abs card" style="left:128px;top:1476px">
    <div class="icon"><svg width="48" height="48" viewBox="0 0 48 48" fill="none" stroke="#fff" stroke-width="2.5"><rect x="8" y="18" width="32" height="22"/><path d="M16 18V10h16v8M16 26h4M28 26h4M16 33h4M28 33h4"/></svg></div>
    <h3>e-Parliament</h3>
    <p>Sed ut perspiciatis unde omnis iste natus error sit voluptatem accusantium doloremque laudantium, totam rem aperiam, eaque ipsa quae ab illo inventore veritatis</p>
  </div>
  <div class="abs card" style="left:628px;top:1476px">
    <div class="icon"><svg width="50" height="50" viewBox="0 0 50 50"><path d="M14 36a9 9 0 0 1 1-18 12 12 0 0 1 23 3 8 8 0 0 1-1 15Z" fill="#fff"/></svg></div>
    <h3>Cloud</h3>
    <p>Sed ut perspiciatis unde omnis iste natus error sit voluptatem accusantium doloremque laudantium, totam rem aperiam, eaque ipsa quae ab illo inventore veritatis</p>
  </div>
  <div class="abs card" style="left:128px;top:1698px">
    <div class="icon"><svg width="48" height="48" viewBox="0 0 48 48" fill="none" stroke="#fff" stroke-width="2.5"><rect x="8" y="10" width="32" height="28"/><path d="M14 32l18-18 4 4-18 18h-4z"/></svg></div>
    <h3>Architecture and Design</h3>
    <p>Sed ut perspiciatis unde omnis iste natus error sit voluptatem accusantium doloremque laudantium, totam rem aperiam, eaque ipsa quae ab illo inventore veritatis</p>
  </div>
  <div class="abs card" style="left:628px;top:1698px">
    <div class="icon"><svg width="50" height="50" viewBox="0 0 50 50" fill="none" stroke="#fff" stroke-width="2.5"><rect x="12" y="13" width="26" height="18" rx="1"/><path d="M6 36h38l-3 4H9z"/></svg></div>
    <h3>Software Development</h3>
    <p>Sed ut perspiciatis unde omnis iste natus error sit voluptatem accusantium doloremque laudantium, totam rem aperiam, eaque ipsa quae ab illo inventore veritatis</p>
  </div>

  <div class="abs rocket" style="left:574px;top:1968px" role="img" aria-label="Rocket in flight"></div>

  <!-- what have we done -->
  <div class="abs done-photo" role="img" aria-label="Colleagues discussing plans at a whiteboard"></div>
  <h2 class="abs section-title done-title">WHAT HAVE WE DONE</h2>
  <p class="abs text done-text">Sed ut perspiciatis unde omnis iste natus error sit volupem accuntium dolue laudantium, totam rem aperiam, eaque ipsa quae ab illo inventore veritatis et quasi architecto beatae vitae dicta sunt explicabo. Nemo enim ipsam vtem quia voluptas sit aspernatur aut odit aut fugit, sed quia consequuntur magni dres eos</p>
  <span class="abs btn-outline done-btn">GET MORE INFO</span>

  <!-- how can we help -->
  <svg class="abs help-bg" viewBox="0 0 1200 600" preserveAspectRatio="none" role="img" aria-label="Orange-toned office backdrop">
    <defs><linearGradient id="helpTone" x1="0" y1="0" x2="1" y2="1"><stop offset="0" stop-color="#e8700f"/><stop offset=".5" stop-color="#f08a2c"/><stop offset="1" stop-color="#e36a0e"/></linearGradient></defs>
    <path d="M0 0H1200V570 C1170 590 1150 560 1120 578 S1060 592 1030 572 S970 556 940 576 S880 594 850 574 S790 556 760 578 S700 592 670 572 S610 556 580 576 S520 594 490 574 S430 556 400 578 S340 592 310 572 S250 556 220 576 S160 594 130 574 S70 556 40 578 S10 588 0 580Z" fill="url(#helpTone)"/>
  </svg>
  <div class="abs rocket" style="left:574px;top:2600px" role="img" aria-label="Rocket in flight"></div>
  <h2 class="abs help-title">HOW CAN WE HELP</h2>
  <div class="abs field" style="left:180px;top:2872px;width:410px">First Name</div>
  <div class="abs field" style="left:610px;top:2872px;width:411px">Last Name</div>
  <div class="abs field" style="left:180px;top:2924px;width:410px">Company Name</div>
  <div class="abs field msg" style="left:610px;top:2924px;width:411px">Message :</div>
  <div class="abs field" style="left:180px;top:2976px;width:410px">Email Address</div>
  <div class="abs field" style="left:180px;top:3028px;width:410px">Phone Number</div>
  <div class="abs submit">SUBMIT NOW</div>

  <!-- footer -->
  <div class="abs footer"></div>
  <div class="abs rocket" style="left:984px;top:3320px" role="img" aria-label="Rocket arriving"></div>

  <div class="abs f-title" style="left:143px;top:3320px">SIGN UP FOR <span>NEWSLETTER</span></div>
  <p class="abs f-text" style="left:143px;top:3365px;width:280px">Excepteur sint occaecat cupidatat non proident, sunt in culpa qui officia deserunt</p>
  <div class="abs f-input">Enter email</div>
  <div class="abs f-btn">SIGN UP</div>

  <div class="abs f-title" style="left:490px;top:3320px">CONTACT <span>US</span></div>
  <div class="abs f-text" style="left:490px;top:3378px">
    <div class="contact-row"><svg width="12" height="16" viewBox="0 0 12 16"><path d="M6 0a6 6 0 0 1 6 6c0 4-6 10-6 10S0 10 0 6a6 6 0 0 1 6-6z" fill="#f07a1a"/><circle cx="6" cy="6" r="2" fill="#fff"/></svg><span>TallyForge<br>Geelong VIC 3220</span></div>
    <div class="contact-row" style="margin-top:4px"><svg width="12" height="14" viewBox="0 0 12 14"><path d="M2 0l3 3-1.5 2a8 8 0 0 0 4 4L9 7.5l3 3L10 13C5 13 0 8 0 2z" fill="#f07a1a"/></svg><span>Phone: +61 2 5550 1427</span></div>
    <div class="contact-row"><svg width="12" height="14" viewBox="0 0 12 14"><rect y="3" width="12" height="9" fill="#f07a1a"/><path d="M0 3l6 5 6-5" stroke="#fff" fill="none"/></svg><span>Email: info@tallyforge.com.au</span></div>
    <div class="social" style="margin-top:10px"><i></i><i></i><i></i><i></i></div>
  </div>

  <div class="abs f-title" style="left:792px;top:3320px">QUICK <span>LINKS</span></div>
  <ul class="abs links" style="left:796px;top:3362px">
    <li>Home</li><li>About</li><li>Services</li><li>Our Works</li><li>Careers</li><li>Contact Us</li>
  </ul>

  <p class="abs copy">TallyForge © 2018 All Rights Reserved | Privacy Policy | Terms and Conditions</p>
</div>
</body>
</html>
```